Website design for luxury private hair salon

I'm looking for someone to use my Logo and build me a website for my webpage www.lunetresses.com.au (You can have a look at it as it has every detail I need included on it already), however I want a fresh new appearance and it to look and feel super stylish.

I am thinking colours in black, with silver or white, beautiful hair images like the ones you'll see on the current webpage - the price list as per what you already see.

I will include a copy of my biz card on here, so you can see the feel of the card, and design a website with a similar feel. It is matt black with a foil silver.

Modern, but classic and fresh. I will also need you to be able to publish it to my URL for me as I have no idea how to do this. I need it up and running pronto!

The website will need to be able to be read clearly on all devices incluing smart phones and ipads. The URL is currently registered and hosted by Nimbo Vault

Thinking a Home Page - large logo etc and write up on who and what we offer
Services/Price List page - as per the price list on my current webpage
Contact Page - with a built in contact form.

Target Market(s)

Middle aged, fashionable, stylish women and men who enjoy luxury hair care and styling in an upmarket location.

Industry/Entity Type

Hair And Beauty

Number of Pages Required

3 page

Font styles to use
Other font styles liked:
• see my images for my current logo

Colors
000000
b2b2b2
a54499

Requirements
Must have
• Style
• Fast turnaround
• Be viewable on all devices, PC, ipads, smart phones
• Designer able to upload it so its a running website for me to my URL
Nice to have
• Just a really feminine, stylish website which is easy to read and shows some beautiful images of perfect hair
Should not have
• Browns, reds or orange colours.

```html
<!DOCTYPE html>
<html lang="en">
<head>
<meta charset="utf-8">
<title>Lune Tresses — Private Hair Salon</title>
<link rel="stylesheet" href="https://fonts.googleapis.com/css2?family=Lato:wght@300;400&family=Great+Vibes&display=swap">
<style>
  :root {
    --bg-top: #000000;
    --bg-bottom: #141414;
    --silver: #d4d4d4;
    --silver-soft: #b2b2b2;
    --text: #e6e6e6;
    --rule: #6a6a6a;
    --frame: #cfcfcf;
    --accent: #4b1166;
    --photo-dark: #0c0906;
    --photo-mid: #2a2018;
    --photo-light: #d9c7a0;
  }
  * { margin: 0; padding: 0; box-sizing: border-box; }
  html, body {
    width: 1200px;
    height: 1012px;
    overflow: hidden;
  }
  body {
    background: linear-gradient(180deg, var(--bg-top) 0%, var(--bg-bottom) 100%);
    font-family: "Lato", Arial, sans-serif;
    color: var(--text);
    position: relative;
  }
  .site-header {
    position: absolute;
    top: 0; left: 0;
    width: 1200px;
    text-align: center;
  }
  .brand-name {
    display: block;
    margin-top: 88px;
    font-family: "Lato", Arial, sans-serif;
    font-weight: 300;
    font-size: 70px;
    letter-spacing: 6px;
    color: var(--silver);
    line-height: 1;
  }
  .main-nav {
    position: absolute;
    top: 252px;
    left: 0;
    width: 1200px;
    display: flex;
    justify-content: center;
    gap: 32px;
  }
  .main-nav a {
    color: var(--text);
    text-decoration: none;
    text-transform: uppercase;
    font-size: 17px;
    letter-spacing: 0.3px;
  }
  .hero-photo {
    position: absolute;
    top: 294px;
    left: 47px;
    width: 1106px;
    height: 471px;
    border: 1px solid var(--frame);
    background:
      radial-gradient(ellipse 260px 230px at 62% 50%, var(--photo-light) 0%, rgba(217,199,160,0.45) 45%, rgba(0,0,0,0) 100%),
      radial-gradient(ellipse 500px 300px at 20% 40%, var(--photo-mid) 0%, var(--photo-dark) 100%);
  }
  .about {
    position: absolute;
    top: 786px;
    left: 47px;
    width: 1106px;
    text-align: center;
  }
  .section-title {
    display: flex;
    align-items: center;
    gap: 12px;
    font-family: "Great Vibes", cursive;
    font-weight: 400;
    font-size: 38px;
    color: var(--text);
    line-height: 1.2;
  }
  .section-title::before,
  .section-title::after {
    content: "";
    flex: 1;
    height: 1px;
    background: var(--rule);
  }
  .about-text {
    margin: 12px auto 0;
    width: 1106px;
    font-size: 21px;
    font-weight: 300;
    line-height: 28px;
  }
  .contact-button {
    display: inline-block;
    margin-top: 29px;
    width: 153px;
    height: 46px;
    line-height: 46px;
    background: var(--accent);
    color: var(--text);
    text-decoration: none;
    text-transform: uppercase;
    font-size: 18px;
    border-radius: 3px;
  }
</style>
</head>
<body>
  <header class="site-header">
    <span class="brand-name">Lune Tresses</span>
  </header>

  <nav class="main-nav">
    <a href="#">Home</a>
    <a href="#">Services</a>
    <a href="#">Price List</a>
    <a href="#">Contact Us</a>
  </nav>

  <div class="hero-photo" role="img" aria-label="Photograph of a woman with long, windswept wavy blonde hair against a dark, softly blurred background"></div>

  <section class="about">
    <h2 class="section-title">About Us</h2>
    <p class="about-text">We pride ourselves on being able to offer a private salon experience to our clients in the exclusive suburb of Elmsworth, where your hair design and colouring needs will be met with years of experience and current industry training and knowledge.</p>
    <a class="contact-button" href="#">Contact Us</a>
  </section>
</body>
</html>
```